Training Company Needs a Web Design

We are a Training company that needs a website design completed for us. "The Harbor Loft" The website will be a 'community space' specialising in 'Change and Transformation'. It will be a 'space' where individuals can come to find out 'latest news', upcoming events and courses, chat with others and find 'tools and templates'. They will need to login as a 'Member'.

The final design needs to be professional but have a 'fun and interactive' feel and appeal to our target audience who are predominantly corporate individuals.

Target Market(s)

Corporate Individuals - they may have a Change or Project background

Industry/Entity Type

Business Consultant

Number of Pages Required

3 page

Font styles to use
Sans Serif

Requirements
Must have
• Design for 'Home Page'
• A professional and corporate 'feel' but be fun and interactive.
Nice to have
• A 'sense' of how some of the other pages may be designed or laid out.

```html
<!DOCTYPE html>
<html lang="en">
<head>
<meta charset="utf-8">
<title>The Harbor Loft — Home</title>
<link href="https://fonts.googleapis.com/css2?family=Open+Sans:wght@400;600;700;800&family=Lora:wght@700&display=swap" rel="stylesheet">
<style>
:root{
  --blue:#0d5c96;
  --blue-bright:#1278bd;
  --teal:#3ec8c0;
  --teal-soft:#7fd9d3;
  --dark:#1c1c1c;
  --page:#ececec;
  --text:#333;
  --muted:#666;
  --white:#fff;
  --yellow:#f2c11b;
  --purple:#7b59a8;
}
*{margin:0;padding:0;box-sizing:border-box}
html,body{width:1200px;height:3934px;overflow:hidden}
body{position:relative;background:var(--page);font-family:"Open Sans",Arial,sans-serif;color:var(--text);font-size:15px;line-height:1.5}
.abs{position:absolute}
.photo{position:absolute}

/* top bar */
.topbar{left:0;top:0;width:1200px;height:47px;background:var(--blue)}
.social{position:absolute;right:60px;top:6px;display:flex;gap:14px}
.social span{width:34px;height:34px;border-radius:50%;background:var(--white);display:block}

/* header */
.header{left:0;top:47px;width:1200px;height:175px;background:var(--white)}
.brand{position:absolute;left:59px;top:55px;display:flex;align-items:center;gap:16px}
.brand-dot{width:58px;height:58px;border-radius:50%;background:var(--teal)}
.brand-name{font-size:30px;font-weight:600;color:var(--blue);line-height:1.1;width:180px}
.search{position:absolute;left:787px;top:80px;display:flex}
.search input{width:268px;height:38px;border:0;background:var(--blue);color:#cfe3f2;padding:0 14px;font:13px "Open Sans",sans-serif}
.search button{width:105px;height:38px;border:0;background:var(--teal);color:var(--white);font:700 13px "Open Sans",sans-serif}

/* nav */
.nav{left:59px;top:228px;width:1094px;height:67px;background:var(--dark);display:flex;align-items:center}
.nav a{color:var(--white);text-decoration:none;font-size:14px;font-weight:600;letter-spacing:.5px;padding:0 22px;height:67px;line-height:67px}
.nav a.active{background:var(--blue-bright)}
.side-tab{width:20px;height:60px;background:var(--blue);top:336px}

/* slider */
.slider{left:59px;top:315px;width:1094px;height:433px;background:linear-gradient(135deg,#c9d6df 0%,#8ea3b3 40%,#2d3a48 75%,#5a6b7a 100%)}
.caption{left:87px;top:630px;width:600px;height:100px;background:rgba(0,0,0,.55);color:var(--white);padding:18px 24px;font-size:18px;line-height:1.4}
.dots{right:90px;top:712px;display:flex;gap:10px}
.dots span{width:15px;height:15px;border-radius:50%;background:var(--white);display:block}
.dots span.on{background:#999}

/* headings */
.h2{width:1200px;left:0;text-align:center;font-size:30px;font-weight:800;color:#111;letter-spacing:.5px}
.h2-left{font-size:30px;font-weight:800;color:#111;text-align:center}

/* services */
.service-icon{width:138px;height:138px;border:2px solid #bbb;border-radius:50%;display:flex;align-items:center;justify-content:center;top:905px}
.service-text{top:1108px;width:300px;font-size:16px;line-height:1.45;color:#333}

/* main focus */
.focus-card{top:1357px;height:393px;background:#f6f6f6}
.focus-card.featured{border:8px solid var(--teal);background:var(--white)}
.focus-img{position:absolute;left:0;top:0;width:100%;height:215px}
.focus-body{position:absolute;left:16px;right:16px;top:232px}
.focus-body h3{font-family:"Lora",Georgia,serif;font-size:22px;color:#111;margin-bottom:8px}
.focus-body p{font-size:13px;line-height:1.5;color:#555}
.arrow{top:1525px}

/* team */
.team-frame{top:1940px;width:250px;height:185px;background:var(--teal);border-radius:46% 54% 40% 60% / 58% 42% 58% 42%}
.team-photo{position:absolute;left:14px;top:12px;width:222px;height:160px;border-radius:44% 56% 42% 58% / 56% 44% 56% 44%}
.team-name{top:2148px;font-size:15px;font-weight:700;color:#111}
.team-text{top:2172px;width:260px;font-size:13px;line-height:1.45;color:#444}

/* news */
.date{width:88px;height:88px;border-radius:50%;background:#2a2a2a;color:var(--white);text-align:center;padding-top:12px}
.date b{display:block;font-size:30px;line-height:1}
.date span{font-size:17px;font-weight:700}
.news-text{left:256px;width:390px;font-size:13px;line-height:1.5;color:#555}
.news-text em{display:block;font-style:normal;color:#999;margin-top:4px}
.event-img{left:708px;top:2380px;width:278px;height:158px;border:6px solid var(--teal);background:linear-gradient(135deg,#d6e3ec,#6f8497 60%,#3b4b5a)}
.event-text{left:708px;top:2555px;width:410px;font-size:13px;line-height:1.5;color:#555}

/* testimonial */
.testimonial-band{left:0;top:2695px;width:1200px;height:665px;background:linear-gradient(160deg,#a6e6e0 0%,#7dd6cf 45%,#55bfb8 75%,#8fdcd5 100%)}
.quote{top:2872px;width:334px;height:158px;background:var(--white);padding:18px 20px;font-size:14px;line-height:1.5;color:#444}
.person{top:3049px;display:flex;align-items:center;gap:12px;font-size:15px;color:#333}
.avatar{width:50px;height:50px;border-radius:50%;background:linear-gradient(135deg,#e6c9b3,#8b6a57)}

/* footer */
.footer{left:0;top:3363px;width:1200px;height:571px;background:var(--blue);color:var(--white)}
.footer h2{position:absolute;left:118px;top:38px;font-size:30px;font-weight:400}
.footer .lead{position:absolute;left:118px;top:92px;width:1040px;font-size:15px;line-height:1.55;color:#e3eef7}
.form{position:absolute;left:118px;top:182px;width:570px}
.form .field{height:34px;background:var(--white);margin-bottom:6px;color:#666;font-size:13px;padding:7px 12px}
.form .field.area{height:220px}
.contact{position:absolute;left:708px;top:182px;width:440px;font-size:13px;line-height:1.55;color:#e3eef7}
.contact h4{font-size:15px;font-weight:600;color:var(--white);margin-bottom:6px}
.contact ul{list-style:none;margin-top:16px}
.contact li{display:flex;align-items:center;gap:12px;margin-bottom:6px}
</style>
</head>
<body>

<div class="abs topbar">
  <div class="social"><span></span><span></span><span></span><span></span><span></span></div>
</div>

<header class="abs header">
  <div class="brand"><span class="brand-dot"></span><span class="brand-name">The Harbor Loft</span></div>
  <form class="search"><input type="text" value="Login as a member"><button type="button">LOGIN</button></form>
</header>

<div class="abs side-tab" style="left:0"></div>
<div class="abs side-tab" style="right:0"></div>

<nav class="abs nav">
  <a class="active">HOME</a><a>COURSES</a><a>ABOUT</a><a>NEWS</a><a>CATEGORIES</a><a>CONTACT</a>
</nav>

<div class="abs slider" role="img" aria-label="Photo of business people meeting around an office table"></div>
<div class="abs caption">A journey by which an individual can get to focus, interact, influence and affect change.</div>
<div class="abs dots"><span></span><span></span><span></span><span class="on"></span><span></span></div>

<h2 class="abs h2" style="top:792px">SERVICES</h2>

<div class="abs service-icon" style="left:147px">
  <svg width="64" height="56" viewBox="0 0 64 56"><rect x="2" y="2" width="38" height="26" rx="3" fill="var(--yellow)"/><path d="M10 28 L10 38 L20 28Z" fill="var(--yellow)"/><rect x="24" y="20" width="38" height="24" rx="3" fill="#e0a90c"/><path d="M52 44 L52 54 L42 44Z" fill="#e0a90c"/></svg>
</div>
<div class="abs service-icon" style="left:521px">
  <svg width="60" height="60" viewBox="0 0 60 60"><line x1="16" y1="30" x2="44" y2="14" stroke="var(--teal)" stroke-width="4"/><line x1="16" y1="30" x2="44" y2="46" stroke="var(--teal)" stroke-width="4"/><circle cx="16" cy="30" r="9" fill="var(--teal)"/><circle cx="44" cy="14" r="9" fill="var(--teal)"/><circle cx="44" cy="46" r="9" fill="var(--teal)"/></svg>
</div>
<div class="abs service-icon" style="left:895px">
  <svg width="64" height="52" viewBox="0 0 64 52"><path d="M4 6 Q18 2 31 8 L31 48 Q18 42 4 46Z" fill="var(--purple)"/><path d="M60 6 Q46 2 33 8 L33 48 Q46 42 60 46Z" fill="#9275bd"/></svg>
</div>
<p class="abs service-text" style="left:118px">Curabitur vestibulum eget mauris quis laoreet. Phasellus in quam laoreet, viverra lacus ut, ultrices velit.</p>
<p class="abs service-text" style="left:472px">Curabitur vestibulum eget mauris quis laoreet. Phasellus in quam laoreet, viverra lacus ut, ultrices velit.</p>
<p class="abs service-text" style="left:870px">Curabitur vestibulum eget mauris quis laoreet. Phasellus in quam laoreet, viverra lacus ut, ultrices velit.</p>

<h2 class="abs h2" style="top:1268px">MAIN FOCUS</h2>

<svg class="abs arrow" style="left:60px" width="22" height="34" viewBox="0 0 22 34"><path d="M18 2 L4 17 L18 32" fill="none" stroke="#c0392b" stroke-width="5"/></svg>
<svg class="abs arrow" style="left:1122px" width="22" height="34" viewBox="0 0 22 34"><path d="M4 2 L18 17 L4 32" fill="none" stroke="#c0392b" stroke-width="5"/></svg>

<article class="abs focus-card" style="left:118px;width:275px">
  <div class="focus-img" role="img" aria-label="Photo of a smiling businesswoman at work" style="background:linear-gradient(135deg,#f3ece4,#b9a593 55%,#5e5048)"></div>
  <div class="focus-body"><h3>Our Passion</h3><p>A unique community space built for practitioners to share transformation practice, change management, tools and project methodologies.</p></div>
</article>
<article class="abs focus-card featured" style="left:460px;width:287px">
  <div class="focus-img" role="img" aria-label="Photo of colleagues collaborating at a desk" style="background:linear-gradient(135deg,#e7d9c2,#a58a63 55%,#4c3d2d)"></div>
  <div class="focus-body"><h3>Our Support</h3><p>The Harbor Loft offers online guidance on a range of training, mentoring, networking and sharing.</p></div>
</article>
<article class="abs focus-card" style="left:799px;width:271px">
  <div class="focus-img" role="img" aria-label="Photo of a business team in a meeting" style="background:linear-gradient(135deg,#efe6da,#9f8b74 55%,#3f352c)"></div>
  <div class="focus-body"><h3>Our Reliability</h3><p>It's a resource for change professionals to follow the conversation around change.</p></div>
</article>

<h2 class="abs h2" style="top:1788px">OUR TEAM</h2>

<div class="abs team-frame" style="left:146px"><div class="team-photo" role="img" aria-label="Portrait of a team member" style="background:linear-gradient(135deg,#d8b9a0,#8a6550 60%,#3c2a20)"></div></div>
<div class="abs team-frame" style="left:472px"><div class="team-photo" role="img" aria-label="Portrait of a team member" style="background:linear-gradient(135deg,#e4c4ab,#a0735a 60%,#4a2f22)"></div></div>
<div class="abs team-frame" style="left:806px"><div class="team-photo" role="img" aria-label="Portrait of a team member" style="background:linear-gradient(135deg,#ecd0b8,#b0826a 60%,#5a3a2b)"></div></div>

<div class="abs team-name" style="left:118px">Carl Brenner</div>
<p class="abs team-text" style="left:118px">Aenean tortor, quam eget molestie non, metus lacus enim curatur purus, non rutrum ullamcorper lorem.</p>
<div class="abs team-name" style="left:488px">Nora Whitfield</div>
<p class="abs team-text" style="left:488px">Aenean tortor, quam eget molestie non, metus lacus enim curatur purus, non rutrum lorem.</p>
<div class="abs team-name" style="left:838px">Elsa Marlow</div>
<p class="abs team-text" style="left:838px">Aenean tortor, quam eget molestie non, metus lacus enim curatur purus, non rutrum ullamcorper lorem.</p>

<h2 class="abs h2-left" style="left:118px;width:400px;top:2300px">LATEST NEWS</h2>
<h2 class="abs h2-left" style="left:690px;width:440px;top:2300px">UPCOMING EVENT</h2>

<div class="abs date" style="left:133px;top:2376px"><b>28</b><span>June</span></div>
<p class="abs news-text" style="top:2378px">Vestibulum ante ipsum primis in faucibus orci luctus et ultrices posuere cubilia curae. Nam id turpis vel sem feugiat sodales at eget risus. Integer luctus.<em>Read more</em></p>
<div class="abs date" style="left:133px;top:2553px"><b>30</b><span>March</span></div>
<p class="abs news-text" style="top:2555px">Vestibulum ante ipsum primis in faucibus orci luctus et ultrices posuere cubilia curae. Nam id turpis vel sem feugiat sodales at eget risus. Integer luctus.<em>Read more</em></p>

<div class="abs event-img" role="img" aria-label="Photo of business people shaking hands at an event"></div>
<p class="abs event-text">Vestibulum ante ipsum primis in faucibus orci luctus et ultrices posuere cubilia curae. Nam id turpis vel sem feugiat sodales at eget risus. Integer luctus mauris.</p>

<div class="abs testimonial-band" role="img" aria-label="Teal-tinted photo of people working at laptops"></div>
<h2 class="abs h2" style="top:2752px">TESTIMONIAL</h2>

<blockquote class="abs quote" style="left:118px">Startup is really a great template to get started with. With its awesome features and easy customisation, this template made my day. Very recommended.</blockquote>
<blockquote class="abs quote" style="left:472px">Startup is really a great template to get started with. With its awesome features and easy customisation, this template made my day. Very recommended.</blockquote>
<blockquote class="abs quote" style="left:826px">Startup is really a great template to get started with. With its awesome features and easy customisation, this template made my day. Very recommended.</blockquote>

<div class="abs person" style="left:130px"><span class="avatar" role="img" aria-label="Client portrait"></span>Peter Lanning</div>
<div class="abs person" style="left:490px"><span class="avatar" role="img" aria-label="Client portrait"></span>Rosa Delacourt</div>
<div class="abs person" style="left:845px"><span class="avatar" role="img" aria-label="Client portrait"></span>Owen Haskell</div>

<footer class="abs footer">
  <h2>Courses</h2>
  <p class="lead">Fusce dapibus, tellus ac cursus commodo, tortor mauris condimentum. Duis mollis, non commodo luctus, nisi erat porttitor ligula, eget lacinia odio sem nec elit. Fusce dapibus, tellus ac cursus commodo, tortor mauris condimentum nibh.</p>
  <div class="form">
    <div class="field">Name (Required)</div>
    <div class="field">Email (Required)</div>
    <div class="field">Subject</div>
    <div class="field area">Details</div>
  </div>
  <div class="contact">
    <h4>Contact Information</h4>
    <p>Aenean tincidunt justo dapibus, ornare velit. Vel turpis aliquet. Nam mollis metus, nec imperdiet ipsum. Nulla sed nisi, et ornare sed ac consequat nisi.</p>
    <ul>
      <li><svg width="14" height="16" viewBox="0 0 14 16"><path d="M7 1a5 5 0 0 1 5 5c0 4-5 9-5 9S2 10 2 6a5 5 0 0 1 5-5z" fill="#fff"/></svg>12 Quay Street, Harbour Side</li>
      <li><svg width="14" height="14" viewBox="0 0 14 14"><path d="M3 1l3 3-2 2c1 2 2 3 4 4l2-2 3 3-2 2C6 13 1 8 1 3z" fill="#fff"/></svg>(012) 555 0148</li>
      <li><svg width="14" height="12" viewBox="0 0 14 12"><rect x="1" y="1" width="12" height="10" fill="none" stroke="#fff" stroke-width="1.5"/><path d="M1 1l6 5 6-5" fill="none" stroke="#fff" stroke-width="1.5"/></svg>hello@harborloft.test</li>
    </ul>
  </div>
</footer>

</body>
</html>
```